Need Help having my business card stand out

I am the owner of Pine Ridge Canine Coaching and would like for my business cards to stand out. I have been trying to keep designing them myself but I can't get what I have in my head on the card. I will try my best to post templates that I like for inspirations. I want something unique but elegant. I don't want in to look cartoony or cheesy. It needs to pop in a pet shop but also in a coffee shop or gym.

Target Market(s)

Dog owners, Married ,No young kids Jr High school kids and up (maybe kids on the way) Executives, Stay at home moms/wives, Small business owners

Industry/Entity Type

Dog Training

Contact Information for Business Card

Trevor Holloway, 555-304-7162, info@pineridgecanine.example, www.pineridgecanine.example

Colors

Designer to choose colors to be used in the design.

Requirements
Must have
• my logo
Should not have
• Cursive lettering

```html
<!DOCTYPE html>
<html lang="en">
<head>
<meta charset="UTF-8">
<title>Pine Ridge Canine Coaching – Business Card</title>
<link rel="stylesheet" href="https://fonts.googleapis.com/css2?family=Montserrat:wght@700;800;900&display=swap">
<style>
  :root {
    --rust: #6e2412;
    --ink: #0d0d0d;
    --paper: #ffffff;
    --shadow: #a6a6a6;
    --edge: #3a3a3a;
  }
  * { margin: 0; padding: 0; box-sizing: border-box; }
  html, body {
    width: 769px;
    height: 1200px;
    overflow: hidden;
    background: var(--paper);
    font-family: "Montserrat", Arial, sans-serif;
  }
  .canvas { position: relative; width: 769px; height: 1200px; }

  .card {
    position: absolute;
    background: var(--paper);
    border: 1.5px solid var(--edge);
    overflow: hidden;
  }
  .card--front {
    left: 17px; top: 17px; width: 742px; height: 431px;
    box-shadow: 12px 12px 0 var(--shadow);
  }
  .card--back {
    left: 16px; top: 732px; width: 751px; height: 446px;
    box-shadow: -10px 10px 0 var(--shadow);
  }

  .brand-disc {
    position: absolute;
    left: 159px; top: -22px;
    width: 416px; height: 416px;
    transform: translateY(8px);
    border-radius: 50%;
    background: var(--rust);
    display: flex; align-items: center; justify-content: center;
  }
  .brand-disc__name {
    color: var(--paper);
    font-weight: 800;
    font-size: 46px;
    line-height: 1.12;
    text-align: center;
    text-transform: uppercase;
    letter-spacing: 1px;
  }

  .silhouette-panel {
    position: absolute;
    left: 0; top: 0;
    width: 270px; height: 100%;
  }

  .contact {
    position: absolute;
    left: 320px; right: 10px; top: 40px;
    text-align: center;
  }
  .contact__brand {
    font-weight: 800;
    font-size: 38px;
    line-height: 1.05;
    color: var(--ink);
    text-transform: uppercase;
  }
  .contact__person {
    margin-top: 36px;
    font-weight: 800;
    font-size: 36px;
    color: var(--ink);
    text-transform: uppercase;
    letter-spacing: 1px;
  }
  .contact__phone {
    margin-top: 24px;
    font-weight: 800;
    font-size: 40px;
    color: var(--rust);
    letter-spacing: 2px;
  }
  .contact__line {
    margin-top: 26px;
    font-weight: 800;
    font-size: 23px;
    color: var(--ink);
  }
  .contact__line + .contact__line { margin-top: 18px; }
</style>
</head>
<body>
<main class="canvas">

  <section class="card card--front" aria-label="Card front">
    <div class="brand-disc">
      <p class="brand-disc__name">Pine Ridge<br>Canine<br>Coaching</p>
    </div>
  </section>

  <section class="card card--back" aria-label="Card back">
    <svg class="silhouette-panel" viewBox="0 0 270 446" role="img" aria-label="Dog head silhouette in profile">
      <path d="M0 0 H270 V140 C250 200 215 250 230 320 C240 370 255 410 265 446 H0 Z" fill="var(--rust)"/>
    </svg>
    <div class="contact">
      <p class="contact__brand">Pine Ridge<br>Canine Coaching</p>
      <p class="contact__person">Trevor Holloway</p>
      <p class="contact__phone">555-304-7162</p>
      <p class="contact__line">info@pineridgecanine.example</p>
      <p class="contact__line">www.pineridgecanine.example</p>
    </div>
  </section>

</main>
</body>
</html>
```